Quillstone Restaurnt Lunch Menu Redesign:

We have two lunch special menus that need to be reformatted into a 4.25inx11in and need a graphics design update. Some menu items need to change and some descriptions need to updated. This new menu should double sided with the Main Dining Lunch Menu on the front side and Teppanyaki Lunch menu on the back.

Both menus should follow the same design formatting as the main dining lunch menu (font, sizing, ect.)

```html
<!DOCTYPE html>
<html lang="en">
<head>
<meta charset="utf-8">
<title>Lunch Menus</title>
<link href="https://fonts.googleapis.com/css2?family=Anton&family=Bebas+Neue&family=Oswald:wght@400;500;600&family=Barlow:wght@400;500&family=Kaushan+Script&display=swap" rel="stylesheet">
<style>
:root{
  --backdrop:#dcdcdc;
  --board:#1d1d1d;
  --board-light:#2a2a2a;
  --ink:#ffffff;
  --ink-soft:#e6e6e6;
  --accent:#f7941d;
  --rule:#8a8a8a;
  --onion:#a8477f;
  --pepper:#e5411b;
  --parsley:#4d9629;
}
*{margin:0;padding:0;box-sizing:border-box}
html,body{width:1040px;height:1200px;overflow:hidden;background:var(--backdrop)}
.menu{position:absolute;top:87px;width:396px;height:1026px;overflow:hidden;
  background:radial-gradient(ellipse at 50% 40%,var(--board-light),var(--board) 75%);
  box-shadow:0 4px 18px rgba(0,0,0,.35);color:var(--ink);font-family:'Barlow',sans-serif}
.menu--dining{left:84px}
.menu--teppanyaki{left:559px}
.abs{position:absolute}
.title{left:0;width:100%;text-align:center;font-family:'Anton',sans-serif;line-height:1;color:var(--ink-soft);text-transform:uppercase}
.script{left:0;width:100%;text-align:center;font-family:'Kaushan Script',cursive;color:var(--accent);line-height:1;text-shadow:0 0 6px #000,0 0 2px #000}
.tagbox{border:1px solid var(--rule);text-align:center;font-family:'Bebas Neue',sans-serif;color:var(--ink);text-transform:uppercase;display:flex;align-items:center;justify-content:center;letter-spacing:.5px;white-space:nowrap;line-height:1;padding-top:3px}
.tagbox b{color:var(--accent);font-weight:400;margin-left:6px}
.frame{border:1px solid var(--rule)}
.frame--double{outline:1px solid var(--rule);outline-offset:-4px}
.section-head{font-family:'Oswald',sans-serif;font-weight:600;color:var(--accent);text-transform:uppercase;font-size:26px;line-height:1;background:var(--board);padding:0 6px 0 2px;left:55px}
.note{left:57px;width:290px;font-size:11px;line-height:14.5px;color:var(--ink-soft)}
.note b{color:var(--accent);font-weight:500}
.row{left:57px;width:283px;height:16px;display:flex;align-items:flex-end;font-size:12.5px;line-height:16px}
.menu--teppanyaki .row{left:56px;width:282px}
.row .leader{flex:1;border-bottom:1px solid #6a6a6a;margin:0 8px 3px}
.row .price{color:var(--accent);font-size:13.5px;line-height:16px}
.row .price sup{font-size:7px;vertical-align:6px;line-height:0}
.desc{left:58px;font-size:8.5px;color:var(--accent);line-height:10px;white-space:nowrap}
.roll{font-size:12.5px;line-height:16px;white-space:nowrap}
.roll small{color:var(--accent);font-size:8px;margin-right:6px}
.center-note{left:0;width:100%;text-align:center;font-size:11px;color:var(--ink-soft)}
.deco{border-radius:50%}
.deco--onion{border:7px solid var(--onion);background:transparent}
.deco--pepper{background:var(--pepper);border-radius:40% 60% 55% 45%}
.deco--parsley{background:var(--parsley);border-radius:45% 55% 50% 50%}
</style>
</head>
<body>

<section class="menu menu--dining">
  <div class="abs deco deco--onion" style="left:-14px;top:92px;width:58px;height:56px" role="img" aria-label="Red onion rings"></div>
  <div class="abs deco deco--pepper" style="left:342px;top:136px;width:48px;height:40px" role="img" aria-label="Red pepper slice"></div>

  <h1 class="abs title" style="top:24px;font-size:132px;letter-spacing:-2px">Lunch</h1>
  <div class="abs script" style="top:58px;font-size:56px">Specials</div>
  <div class="abs tagbox" style="left:53px;top:155px;width:289px;height:39px;font-size:30px">Served daily <b>11am - 3pm</b></div>

  <div class="abs frame" style="left:40px;top:225px;width:318px;height:183px"></div>
  <h2 class="abs section-head" style="top:211px">Sandwiches</h2>
  <p class="abs note" style="top:241px">Served with Choice of Miso Soup or House Salad &amp; Potato Chips</p>
  <div class="abs row" style="top:273px"><span>Fried Breaded Calamari Steak</span><span class="leader"></span><span class="price"><sup>$</sup>16</span></div>
  <div class="abs desc" style="top:290px">with Tomato, Lettuce &amp; Onion</div>
  <div class="abs row" style="top:306px"><span>Grilled Chicken</span><span class="leader"></span><span class="price"><sup>$</sup>16</span></div>
  <div class="abs desc" style="top:323px">with Bacon, Tomato, Lettuce &amp; Mayonnaise Drizzle</div>
  <div class="abs row" style="top:337px"><span>Hamburger</span><span class="leader"></span><span class="price"><sup>$</sup>18</span></div>
  <div class="abs desc" style="top:354px">with Lettuce, Tomato, Onion, Mayonnaise Drizzle</div>
  <div class="abs row" style="top:370px"><span>Fried Soft Shell Crab Burger</span><span class="leader"></span><span class="price"><sup>$</sup>20</span></div>
  <div class="abs desc" style="top:387px">with Avocado, Lettuce, Tomato, Onion &amp; Mayo</div>

  <div class="abs deco deco--pepper" style="left:-10px;top:380px;width:52px;height:48px" role="img" aria-label="Red pepper slice"></div>

  <div class="abs frame" style="left:40px;top:438px;width:318px;height:152px"></div>
  <h2 class="abs section-head" style="top:425px">Sushi Specials</h2>
  <p class="abs note" style="top:452px">Please Select 4 of the followings for <b>$ 16</b><br>Served with a 4 piece California Roll &amp; Miso Soup or House Salad</p>
  <div class="abs roll" style="left:57px;top:501px">Hamachi<small> Yellowtail Tuna</small> Hotate<small> Scallop</small> Ika<small> Squid</small></div>
  <div class="abs roll" style="left:57px;top:520px">Ikura<small> Salmon Roe</small> Saba<small> Mackerel</small> Sake<small> Salmon</small> Tai<small> Red Snapper</small></div>
  <div class="abs" style="left:57px;top:538px;width:283px;border-top:1px solid #6a6a6a"></div>
  <div class="abs roll" style="left:57px;top:543px">Maguro<small> Yellow fin Tuna</small></div>
  <div class="abs roll" style="left:57px;top:562px">Smoked Salmon</div>
  <div class="abs" style="left:174px;top:546px;height:28px;border-left:1px solid #8a8a8a"></div>
  <div class="abs roll" style="left:186px;top:545px">Tako<small> Octopus</small> Ebi<small> Shrimp</small></div>
  <div class="abs roll" style="left:186px;top:564px">Unagi<small> BBQ Eel</small> Tamago<small> Egg</small></div>

  <div class="abs deco deco--onion" style="left:362px;top:580px;width:52px;height:60px" role="img" aria-label="Red onion ring"></div>
  <div class="abs deco deco--parsley" style="left:-6px;top:597px;width:50px;height:48px" role="img" aria-label="Parsley sprig"></div>

  <div class="abs frame" style="left:40px;top:622px;width:318px;height:321px"></div>
  <h2 class="abs section-head" style="top:608px">Main Courses</h2>
  <p class="abs note" style="top:638px">Served with Rice &amp; Choice of Miso Soup or House Salad<br>All Meals Served with Rice. Upgrade to fried rice<br>for only <b>$4</b></p>
  <div class="abs row" style="top:685px"><span>Organic Tofu Teriyaki</span><span class="leader"></span><span class="price"><sup>$</sup>14</span></div>
  <div class="abs desc" style="top:702px">Served Grilled or Tempura Fried</div>
  <div class="abs row" style="top:718px"><span>Chicken Teriyaki</span><span class="leader"></span><span class="price"><sup>$</sup>16</span></div>
  <div class="abs row" style="top:742px"><span>Spicy Chicken Teriyaki</span><span class="leader"></span><span class="price"><sup>$</sup>16</span></div>
  <div class="abs row" style="top:767px"><span>Beef Teriyaki</span><span class="leader"></span><span class="price"><sup>$</sup>16</span></div>
  <div class="abs row" style="top:791px"><span>Spicy Beef Teriyaki</span><span class="leader"></span><span class="price"><sup>$</sup>16</span></div>
  <div class="abs row" style="top:816px"><span>Chicken Katsu</span><span class="leader"></span><span class="price"><sup>$</sup>15</span></div>
  <div class="abs desc" style="top:833px">Breaded Chicken Breast</div>
  <div class="abs row" style="top:847px"><span>Katsu Don</span><span class="leader"></span><span class="price"><sup>$</sup>16</span></div>
  <div class="abs desc" style="top:864px">Fried Chicken Breast, Egg &amp; Onion over Rice</div>
  <div class="abs row" style="top:878px"><span>Unagi Don</span><span class="leader"></span><span class="price"><sup>$</sup>19</span></div>
  <div class="abs desc" style="top:895px">BBQ Eel over Rice</div>
  <div class="abs row" style="top:911px"><span>Shrimp &amp; Vegetable Tempura</span><span class="leader"></span><span class="price"><sup>$</sup>16</span></div>

  <div class="abs deco deco--onion" style="left:-8px;top:940px;width:60px;height:60px" role="img" aria-label="Red onion rings"></div>
  <div class="abs" style="left:100px;top:962px;width:196px;border-top:1px solid #8a6a3a"></div>
  <div class="abs center-note" style="top:953px"><span style="background:var(--board);padding:0 6px;font-family:'Oswald',sans-serif;color:var(--accent);font-size:15px;text-transform:uppercase;font-weight:500">Served Raw</span></div>
  <div class="abs center-note" style="top:971px;font-size:12px;color:var(--ink)"><b style="color:var(--accent);font-weight:500">20%</b> gratuity added to parties of <span style="color:var(--accent)">6</span> or more.</div>
  <div class="abs center-note" style="top:987px;font-size:8.2px">Consuming raw or undercooked food may increase your risk of foodborne illness</div>
  <div class="abs deco deco--parsley" style="left:336px;top:1000px;width:64px;height:36px" role="img" aria-label="Parsley sprig"></div>
</section>

<section class="menu menu--teppanyaki">
  <div class="abs deco deco--onion" style="left:-14px;top:88px;width:58px;height:56px" role="img" aria-label="Red onion rings"></div>
  <div class="abs deco deco--pepper" style="left:344px;top:120px;width:50px;height:52px" role="img" aria-label="Red pepper slice"></div>

  <h1 class="abs title" style="top:30px;font-size:70px;color:var(--ink)">Teppanyaki</h1>
  <div class="abs script" style="top:58px;font-size:56px">Lunch</div>
  <div class="abs tagbox" style="left:53px;top:127px;width:290px;height:38px;font-size:30px">Available until <b>11-2:30pm</b></div>
  <p class="abs center-note" style="top:173px">Served with Miso Soup or Salad, Choice of Rice &amp; Vegetables</p>

  <div class="abs frame frame--double" style="left:39px;top:204px;width:319px;height:409px"></div>
  <div class="abs row" style="top:219px"><span>Hibachi Chicken</span><span class="leader"></span><span class="price"><sup>$</sup>18</span></div>
  <div class="abs row" style="top:245px"><span>Hibachi Shrimp</span><span class="leader"></span><span class="price"><sup>$</sup>19</span></div>
  <div class="abs row" style="top:271px"><span>Hibachi New York Steak</span><span class="leader"></span><span class="price"><sup>$</sup>20</span></div>
  <div class="abs row" style="top:297px"><span>Hibachi Salmon</span><span class="leader"></span><span class="price"><sup>$</sup>20</span></div>
  <div class="abs row" style="top:323px"><span>Teriyaki Beef</span><span class="leader"></span><span class="price"><sup>$</sup>19</span></div>
  <div class="abs row" style="top:348px"><span>Hibachi Scallop</span><span class="leader"></span><span class="price"><sup>$</sup>20</span></div>
  <div class="abs row" style="top:374px"><span>Chicken and Shrimp</span><span class="leader"></span><span class="price"><sup>$</sup>21</span></div>
  <div class="abs row" style="top:401px"><span>Scallop and Shrimp</span><span class="leader"></span><span class="price"><sup>$</sup>22</span></div>
  <div class="abs row" style="top:426px"><span>New York Steak and Chicken</span><span class="leader"></span><span class="price"><sup>$</sup>22</span></div>
  <div class="abs row" style="top:452px"><span>New York Steak and Shrimp</span><span class="leader"></span><span class="price"><sup>$</sup>23</span></div>
  <div class="abs row" style="top:478px"><span>New York Steak and Scallop</span><span class="leader"></span><span class="price"><sup>$</sup>24</span></div>
  <div class="abs row" style="top:504px"><span>Filet Mignon</span><span class="leader"></span><span class="price"><sup>$</sup>23</span></div>
  <div class="abs row" style="top:530px"><span>Filet Mignon and Chicken</span><span class="leader"></span><span class="price"><sup>$</sup>25</span></div>
  <div class="abs row" style="top:556px"><span>Filet Mignon and Shrimp</span><span class="leader"></span><span class="price"><sup>$</sup>26</span></div>
  <div class="abs row" style="top:582px"><span>Filet Mignon and Scallop</span><span class="leader"></span><span class="price"><sup>$</sup>27</span></div>

  <div class="abs deco deco--parsley" style="left:6px;top:622px;width:55px;height:56px" role="img" aria-label="Parsley sprig"></div>
  <div class="abs deco deco--onion" style="left:338px;top:598px;width:66px;height:74px" role="img" aria-label="Red onion ring"></div>

  <h2 class="abs title" style="top:634px;font-size:74px;color:var(--ink)">Spacial</h2>
  <div class="abs script" style="top:680px;font-size:56px;padding-left:12px">Menu</div>
  <div class="abs tagbox" style="left:39px;top:742px;width:319px;height:32px;font-size:22px;letter-spacing:.2px;background:var(--board)">Ages 12 and under ~ Ages 65 and older</div>
  <p class="abs center-note" style="top:782px">Served with Miso Soup or Salad, Choice of Rice &amp; Vegetables</p>

  <div class="abs frame frame--double" style="left:39px;top:815px;width:319px;height:172px"></div>
  <div class="abs row" style="top:830px"><span>Hibachi Chicken</span><span class="leader"></span><span class="price"><sup>$</sup>15</span></div>
  <div class="abs row" style="top:855px"><span>Hibachi Shrimp</span><span class="leader"></span><span class="price"><sup>$</sup>16</span></div>
  <div class="abs row" style="top:880px"><span>Hibachi Scallop</span><span class="leader"></span><span class="price"><sup>$</sup>18</span></div>
  <div class="abs row" style="top:904px"><span>Hibachi New York Steak</span><span class="leader"></span><span class="price"><sup>$</sup>18</span></div>
  <div class="abs row" style="top:929px"><span>Hibachi Scallop</span><span class="leader"></span><span class="price"><sup>$</sup>18</span></div>
  <div class="abs row" style="top:954px"><span>Teriyaki Beef</span><span class="leader"></span><span class="price"><sup>$</sup>16</span></div>

  <div class="abs deco deco--onion" style="left:-10px;top:945px;width:54px;height:62px" role="img" aria-label="Red onion rings"></div>
  <div class="abs deco deco--parsley" style="left:338px;top:996px;width:62px;height:36px" role="img" aria-label="Parsley sprig"></div>
</section>

</body>
</html>
```